Profi-Kistenhof
Zielgruppe
Profi-Kistenhof.de vermietet Lagercontainern an Privatkunden und Gewerbetriebende
Vermietung von Stellfächen für Wohnmobile/Boote etc
Das ganze auf einem Gewerbegelände in Köln (Brauweiler)
Aufgabenstellung
Erstellung eines 2-Seitigen DIN lang (10,5 x 21 cm) Flyers
Seite A: Vermietung von Lagercontainern
Seite B: Stellfächen für Wohnmobile/Boote
Wichtig: Die Sicherheit (Zutrittskontrolle, Videoüberwachung, Brandmeldeanlage)
Preise sollen auf Flyern erscheinen, diese wie auch die Textee möchte ich jedoch ändern können.
Alle Texte können auch von der Seite profi-kistenhof.de übernommen werden
Das Logo (siehe boxen_welten.ai) müsste noch bearbeitet werden .... also "boxenwelten" raus und dafür "Lagerraum Container" rein
Gerne mit Symbolen arbeiten ..

```html
<!DOCTYPE html>
<html lang="de">
<head>
<meta charset="utf-8">
<title>Profi-Kistenhof – Vermietung von Lagercontainern</title>
<link rel="stylesheet" href="https://fonts.googleapis.com/css2?family=Barlow+Condensed:wght@500;600;700&family=Source+Sans+3:wght@400;600;700&display=swap">
<style>
  :root{
    --navy:#1b2f52;
    --navy-deep:#152845;
    --red:#a3162f;
    --orange:#f07a12;
    --white:#ffffff;
    --paper-top:#ffffff;
    --paper-bottom:#e6e9ee;
    --ink:#1b2f52;
    --muted:#8a93a3;
    --head-font:"Barlow Condensed", "Arial Narrow", sans-serif;
    --body-font:"Source Sans 3", Arial, sans-serif;
  }
  *{box-sizing:border-box;margin:0;padding:0}
  html,body{width:1200px;height:2400px;overflow:hidden}
  body{font-family:var(--body-font);color:var(--ink);background:var(--white)}
  .flyer{position:relative;width:1200px;height:2400px;overflow:hidden;
    background:linear-gradient(180deg,var(--paper-top) 1020px,var(--paper-bottom) 2230px)}

  /* header */
  .masthead{position:absolute;left:0;top:0;width:1200px;height:334px;background:var(--navy)}
  .brand-frame{position:absolute;left:100px;top:54px;width:1000px;height:236px;
    border:5px solid var(--white);border-radius:26px;display:flex;align-items:center;justify-content:center;gap:40px}
  .brand-mark{width:96px;height:96px;background:var(--red);border-radius:10px}
  .brand-name{font-family:var(--head-font);font-weight:600;font-size:118px;color:var(--white);letter-spacing:2px;line-height:1}

  .claim-band{position:absolute;left:0;top:348px;width:1200px;height:146px;background:var(--red);
    display:flex;align-items:center;justify-content:center;gap:64px}
  .claim{display:flex;align-items:center;gap:18px;color:var(--white);font-family:var(--body-font);font-weight:600;font-size:68px;line-height:1}
  .claim svg{width:54px;height:54px}

  /* photo */
  .site-photo{position:absolute;left:0;top:500px;width:1200px;height:516px;
    background:linear-gradient(180deg,#8fb0d8 0%,#b5cbe4 30%,#2f4f86 55%,#26467d 72%,#6b5a46 82%,#4e4234 100%)}

  .offer-badge{position:absolute;left:58px;top:522px;width:446px;height:446px;border-radius:50%;
    background:radial-gradient(circle,#f4f4f4 60%,#c9ccd1 100%);box-shadow:0 6px 18px rgba(0,0,0,.35)}
  .offer-badge-inner{position:absolute;left:22px;top:22px;width:402px;height:402px;border-radius:50%;background:var(--orange);
    display:flex;flex-direction:column;align-items:center;justify-content:center;color:var(--white);text-align:center;transform:rotate(-11deg)}
  .offer-title{font-family:var(--head-font);font-weight:700;font-size:80px;line-height:.92;letter-spacing:1px}
  .offer-note{font-family:var(--body-font);font-weight:600;font-size:36px;line-height:1.15;margin-top:12px}

  /* main */
  .section-title{position:absolute;left:0;top:1060px;width:1200px;text-align:center;font-family:var(--head-font);
    font-weight:600;font-size:84px;letter-spacing:2px;color:var(--navy);line-height:1}

  .container-visual{position:absolute;left:70px;top:1180px;width:510px;height:420px;
    background:linear-gradient(90deg,#22458c 0%,#2b53a0 45%,#b8844d 52%,#c99a62 60%,#dfe2e6 72%,#c7cbd1 100%);
    border-radius:4px;box-shadow:0 24px 30px -18px rgba(0,0,0,.35)}

  .price-card{position:absolute;left:619px;top:1200px;width:532px;height:378px;background:var(--navy);border-radius:20px;padding:10px}
  .price-card-inner{width:100%;height:100%;border:2px solid var(--white);border-radius:14px;padding:26px 0 0 46px;color:var(--white)}
  .price{font-family:var(--body-font);font-weight:600;font-size:68px;line-height:1}
  .price small{font-size:30px;font-weight:400;margin-left:8px}
  .feature-list{list-style:none;margin-top:20px}
  .feature-list li{display:flex;align-items:center;gap:12px;font-size:30px;line-height:44px}
  .feature-list svg{width:24px;height:24px;flex:none}

  .info-box{position:absolute;left:43px;top:1628px;width:1114px;height:520px;background:var(--white);
    border:6px solid var(--navy);border-radius:22px;padding:40px 0 0 50px}
  .info-text{font-size:34px;line-height:60px;color:var(--navy);width:1010px}
  .security-grid{display:grid;grid-template-columns:560px 440px;row-gap:8px;margin-top:26px}
  .security-item{display:flex;align-items:center;gap:20px;font-weight:700;font-size:40px;line-height:56px;color:var(--navy)}
  .security-item svg{width:40px;height:40px;flex:none}

  .footnote{position:absolute;left:90px;top:2178px;font-size:19px;font-weight:600;color:var(--muted)}

  /* footer */
  .contact-bar{position:absolute;left:0;top:2228px;width:1200px;height:172px;background:var(--navy);color:var(--white);padding:34px 0 0 90px}
  .contact-line{display:flex;align-items:center;gap:14px;font-size:34px;line-height:56px;letter-spacing:.5px}
  .contact-line svg{width:26px;height:30px;flex:none}
  .contact-line .gap{margin-left:26px}
</style>
</head>
<body>
<svg width="0" height="0" style="position:absolute">
  <defs>
    <symbol id="tick-circle" viewBox="0 0 24 24"><circle cx="12" cy="12" r="12" fill="#fff"/><path d="M6.5 12.5l3.6 3.6 7.4-7.6" fill="none" stroke="currentColor" stroke-width="3.2" stroke-linecap="round" stroke-linejoin="round"/></symbol>
    <symbol id="ico-camera" viewBox="0 0 24 24"><rect x="1" y="5" width="15" height="14" rx="2" fill="currentColor"/><path d="M17 10l6-4v12l-6-4z" fill="currentColor"/></symbol>
    <symbol id="ico-target" viewBox="0 0 24 24"><circle cx="12" cy="12" r="10" fill="none" stroke="currentColor" stroke-width="2.4"/><circle cx="12" cy="12" r="4.5" fill="currentColor"/></symbol>
    <symbol id="ico-extinguisher" viewBox="0 0 24 24"><rect x="8" y="8" width="8" height="15" rx="3" fill="currentColor"/><rect x="10" y="4" width="4" height="4" fill="currentColor"/><path d="M14 5h5l2 3" fill="none" stroke="currentColor" stroke-width="2"/></symbol>
    <symbol id="ico-lock" viewBox="0 0 24 24"><path d="M7 11V8a5 5 0 0110 0v3" fill="none" stroke="currentColor" stroke-width="2.6"/><rect x="4" y="11" width="16" height="12" rx="2" fill="currentColor"/></symbol>
    <symbol id="ico-speaker" viewBox="0 0 24 24"><path d="M2 9h5l6-5v16l-6-5H2z" fill="currentColor"/><path d="M16 8a5 5 0 010 8M19 5a9 9 0 010 14" fill="none" stroke="currentColor" stroke-width="2" stroke-linecap="round"/></symbol>
    <symbol id="ico-bulb" viewBox="0 0 24 24"><path d="M12 2a7 7 0 00-4 12.7V18h8v-3.3A7 7 0 0012 2z" fill="none" stroke="currentColor" stroke-width="2.2"/><path d="M9 21h6" stroke="currentColor" stroke-width="2.2" stroke-linecap="round"/></symbol>
    <symbol id="ico-pin" viewBox="0 0 20 24"><path d="M10 1a7.5 7.5 0 00-7.5 7.5C2.5 14 10 23 10 23s7.5-9 7.5-14.5A7.5 7.5 0 0010 1z" fill="none" stroke="#fff" stroke-width="2.2"/><circle cx="10" cy="8.5" r="2.6" fill="#fff"/></symbol>
    <symbol id="ico-person" viewBox="0 0 20 24"><circle cx="10" cy="7" r="5" fill="#fff"/><path d="M1 23a9 8 0 0118 0z" fill="#fff"/></symbol>
    <symbol id="ico-mail" viewBox="0 0 26 20"><rect x="1" y="2" width="24" height="16" rx="1.5" fill="none" stroke="#fff" stroke-width="2.2"/><path d="M2 3l11 9 11-9" fill="none" stroke="#fff" stroke-width="2.2"/></symbol>
    <symbol id="ico-globe" viewBox="0 0 24 24"><circle cx="12" cy="12" r="10" fill="none" stroke="#fff" stroke-width="2"/><ellipse cx="12" cy="12" rx="4.5" ry="10" fill="none" stroke="#fff" stroke-width="1.8"/><path d="M2 12h20M4 7h16M4 17h16" stroke="#fff" stroke-width="1.6"/></symbol>
  </defs>
</svg>

<main class="flyer">
  <header class="masthead">
    <div class="brand-frame">
      <span class="brand-mark"></span>
      <span class="brand-name">PROFI-KISTENHOF</span>
    </div>
  </header>

  <div class="claim-band">
    <span class="claim"><svg style="color:var(--red)"><use href="#tick-circle"/></svg>Günstig</span>
    <span class="claim"><svg style="color:var(--red)"><use href="#tick-circle"/></svg>Sicher</span>
    <span class="claim"><svg style="color:var(--red)"><use href="#tick-circle"/></svg>Lagern</span>
  </div>

  <div class="site-photo" role="img" aria-label="Foto: Reihe blauer Lagercontainer auf dem Gelände unter blauem Himmel mit Bäumen"></div>

  <div class="offer-badge">
    <div class="offer-badge-inner">
      <div class="offer-title">1 MONAT<br>KOSTENFREI!</div>
      <div class="offer-note">bei einer Anmietung<br>ab 3 Monaten</div>
    </div>
  </div>

  <h1 class="section-title">VERMIETUNG VON LAGERCONTAINERN</h1>

  <div class="container-visual" role="img" aria-label="Illustration: geöffneter blauer Lagercontainer mit gestapelten Holzkisten"></div>

  <div class="price-card">
    <div class="price-card-inner">
      <div class="price">148,- €<small>pro Monat*</small></div>
      <ul class="feature-list">
        <li><svg style="color:var(--navy)"><use href="#tick-circle"/></svg>Durchgehend zugänglich</li>
        <li><svg style="color:var(--navy)"><use href="#tick-circle"/></svg>14m² Lagerkapazität</li>
        <li><svg style="color:var(--navy)"><use href="#tick-circle"/></svg>Versicherungsschutz möglich</li>
        <li><svg style="color:var(--navy)"><use href="#tick-circle"/></svg>Zutrittskontrolle</li>
        <li><svg style="color:var(--navy)"><use href="#tick-circle"/></svg>Videoüberwachung</li>
      </ul>
    </div>
  </div>

  <section class="info-box">
    <p class="info-text">Profi-Kistenhof vermietet Container zu kleinem Preis und Top-Konditonen für die Lagerung privater oder gewerblicher Güter – auch als kurzfristige Lösung (z.B. bei Umzug) geeignet. Dabei steht bei uns die Sicherheit an erster Stelle.</p>
    <div class="security-grid">
      <div class="security-item"><svg><use href="#ico-camera"/></svg>Videoüberwachung</div>
      <div class="security-item"><svg><use href="#ico-lock"/></svg>Sicherheitsschloss</div>
      <div class="security-item"><svg><use href="#ico-target"/></svg>Zutrittskontrolle</div>
      <div class="security-item"><svg><use href="#ico-speaker"/></svg>Alarmanlage</div>
      <div class="security-item"><svg><use href="#ico-extinguisher"/></svg>Brandmeldeanlage</div>
      <div class="security-item"><svg><use href="#ico-bulb"/></svg>Licht</div>
    </div>
  </section>

  <p class="footnote">*Preis gilt pro Monat und Container für private Vermietung, bei gewerblicher Anmietung zzgl. 19% MwSt</p>

  <footer class="contact-bar">
    <div class="contact-line"><svg><use href="#ico-pin"/></svg>Lindenweg 27 im Gewerbegebiet Nordfeld-Auenhof</div>
    <div class="contact-line">
      <svg><use href="#ico-person"/></svg>02234 5550147
      <svg class="gap" style="width:30px"><use href="#ico-mail"/></svg>info@profi-kistenhof.de
      <svg class="gap"><use href="#ico-globe"/></svg>profi-kistenhof.de
    </div>
  </footer>
</main>
</body>
</html>
```